Label Sticker for Tea Bag and Herbs and Spices Bag

I want to design the product label sticker size in 60 mm (H) x 100 mm (W).
This label is for our product herbal tea bag. We sell herbs such as Rose buds, Lavender, Chamomile, etc they are consider flower tea. Our products are natural dry herbs and spices.
I select Green, Brown, white as color combination. I can accept other colour proposed. If it look nice. However, only maximum 3 colours to play around and white is a compulsory colour.
I will print the product name, description, expiry date and instruction how to use and company name and address on it in black ink.
Prefer the label have natural look.
I would like to place my company logo in the label. Attached is the full colour artwork logo file.
I can accept one colour for logo since I only use 3 maximum colour.

Please advise the best design.

Reason: I am sorry as first time use Maple forum, I am not sure how to use the system.

Target Market(s)

To consumer who drink tea

Industry/Entity Type

It Company

Font styles to use
Serif

Requirements
Must have
• 60 mm (H) x 100 mm (w)
• Maximum 3 colour to play.
• Natural look and attraction to consumers.
Nice to have
• -Some drawing such as flower or leaves, lines, waves... as wallpaper
• -Can use 3 colour to separate Products name, Description and How to use.
• -Can give different colour besides my request for comparison.
• -Nice frame
Should not have
• Big pictures - Because it take the spaces, I cannot write more information in the label
• Too dark colour -Consumer cannot see the product information very clearly
• Too big logo - As it will take the space of the label.

```html
<!DOCTYPE html>
<html lang="en">
<head>
<meta charset="utf-8">
<title>Lavender – Product Label</title>
<link href="https://fonts.googleapis.com/css2?family=Federo&family=PT+Sans+Narrow:wght@400;700&display=swap" rel="stylesheet">
<style>
  :root {
    --backdrop: #707070;
    --label-white: #ffffff;
    --cream: #f6f5df;
    --leaf-green: #b5c132;
    --leaf-green-soft: #d3da7a;
    --rust: #d27e66;
    --ink: #231f20;
  }
  html, body {
    margin: 0;
    width: 1200px;
    height: 851px;
    overflow: hidden;
    background: var(--backdrop);
  }
  .label {
    position: absolute;
    left: 100px;
    top: 126px;
    width: 1000px;
    height: 600px;
    border-radius: 26px;
    background: var(--label-white);
    overflow: hidden;
  }
  .wallpaper {
    position: absolute;
    inset: 0;
    background: radial-gradient(ellipse at 50% 55%, var(--label-white) 0%, var(--cream) 75%);
  }
  .foliage {
    position: absolute;
    background: linear-gradient(180deg, var(--leaf-green) 0%, var(--leaf-green-soft) 100%);
  }
  .foliage--top { left: 0; top: 0; width: 1000px; height: 56px;
    background: linear-gradient(90deg, var(--leaf-green) 0%, var(--leaf-green-soft) 50%, var(--leaf-green) 100%); }
  .foliage--left { left: 0; top: 56px; width: 48px; height: 430px; }
  .foliage--right { right: 0; top: 56px; width: 48px; height: 430px; }
  .frame {
    position: absolute;
    left: 0;
    top: 0;
  }
  .brand {
    position: absolute;
    left: 390px;
    top: 22px;
    width: 220px;
    height: 74px;
    background: var(--label-white);
    display: flex;
    align-items: center;
    justify-content: center;
    gap: 10px;
    font-family: "PT Sans Narrow", sans-serif;
    font-weight: 400;
    font-size: 30px;
    letter-spacing: 1px;
    color: var(--rust);
  }
  .brand__dot {
    width: 12px;
    height: 12px;
    border-radius: 50%;
    background: var(--rust);
  }
  .product-name {
    position: absolute;
    left: 0;
    width: 1000px;
    top: 120px;
    margin: 0;
    text-align: center;
    font-family: "Federo", sans-serif;
    font-weight: 400;
    font-size: 118px;
    line-height: 1;
    color: var(--ink);
  }
  .product-description {
    position: absolute;
    left: 0;
    width: 1000px;
    top: 240px;
    margin: 0;
    text-align: center;
    font-family: "Federo", sans-serif;
    font-size: 32px;
    color: var(--ink);
  }
  .info {
    position: absolute;
    left: 26px;
    right: 26px;
    top: 498px;
    margin: 0;
    text-align: center;
    font-family: "PT Sans Narrow", sans-serif;
    font-size: 17.5px;
    line-height: 28px;
    color: var(--rust);
  }
  .info strong { font-weight: 700; }
  .importer { margin-top: 6px; font-size: 18px; }
</style>
</head>
<body>
  <main class="label">
    <div class="wallpaper" role="img" aria-label="Faint cream swirling leaf wallpaper pattern"></div>
    <div class="foliage foliage--top" role="img" aria-label="Green flourishing leaf ornament along the top edge"></div>
    <div class="foliage foliage--left" role="img" aria-label="Green flourishing leaf ornament along the left edge"></div>
    <div class="foliage foliage--right" role="img" aria-label="Green flourishing leaf ornament along the right edge"></div>

    <svg class="frame" width="1000" height="600" viewBox="0 0 1000 600" aria-hidden="true">
      <g fill="none" stroke="var(--rust)" stroke-width="2">
        <rect x="48" y="56" width="904" height="430" fill="none"/>
        <path d="M58 486 V66 H942 V486"/>
        <line x1="0" y1="486" x2="1000" y2="486"/>
      </g>
    </svg>

    <div class="brand"><span class="brand__dot"></span>MEADOW LEAF</div>

    <h1 class="product-name">LAVENDER</h1>
    <p class="product-description">DESCRIPTION</p>

    <div class="info">
      <p style="margin:0"><strong>HOW TO USE &amp; STORAGE INSTRUCTION:</strong>&nbsp; Measure out 1 rounded teaspoon of tea. Pour freshly boiled water over the tea. Cover and allow to steep for 3 to 5 minutes. Store unused tea in air-tight container in refrigerator. Store in cool, dark and dry area can keep the tea fresh.</p>
      <p class="importer" style="margin-bottom:0"><strong>IMPORTED BY:</strong> MEADOW LEAF PTE LTD,&nbsp; T: 6100 2345,&nbsp; M: 9100 5678,&nbsp; WWW.MEADOWLEAFLIFE.COM.SG</p>
    </div>
  </main>
</body>
</html>
```